GHalvor Busisness Card

I am an aerospace consultant and at this time only need business cards.

Industry/Entity Type

Business

Contact Information for Business Card

Halvorsen Associates,LLC
Marcus D. Halvorsen

348 Birch Meadow Drive
Hartwell AL 35612

256-555-0187 (cell)
256-555-0142 (fax)

marcushalvorsen@mailbrook.test

```html
<!DOCTYPE html>
<html lang="en">
<head>
<meta charset="utf-8">
<title>Halvorsen Associates, LLC – Business Card</title>
<link rel="stylesheet" href="https://fonts.googleapis.com/css2?family=Marcellus&family=Open+Sans:wght@400;600&display=swap">
<style>
  :root {
    --backdrop: #c9c9c9;
    --card-white: #ffffff;
    --brand-blue: #3d5fa8;
    --brand-blue-light: #5a80c8;
    --brand-blue-dark: #2c4786;
    --panel-black: #0f1114;
    --panel-charcoal: #22262b;
    --ink: #111111;
    --name-blue: #3f5a9c;
    --contact-white: #f2f2f2;
  }
  html, body {
    margin: 0;
    padding: 0;
    width: 1200px;
    height: 900px;
    overflow: hidden;
    background: var(--backdrop);
  }
  .business-card {
    position: absolute;
    left: 160px;
    top: 198px;
    width: 880px;
    height: 504px;
    border-radius: 40px;
    overflow: hidden;
    background: var(--card-white);
    box-shadow: 0 18px 40px rgba(0,0,0,0.22);
  }
  .brand-area {
    position: absolute;
    left: 0; top: 0;
    width: 100%;
    height: 232px;
    background: var(--card-white);
  }
  .brand-square {
    position: absolute;
    left: 50px;
    top: 62px;
    width: 112px;
    height: 112px;
    border-radius: 14px;
    background: linear-gradient(160deg, var(--brand-blue-light), var(--brand-blue-dark));
  }
  .brand-name {
    position: absolute;
    left: 186px;
    top: 88px;
    margin: 0;
    font-family: "Marcellus", serif;
    font-weight: 400;
    font-size: 44px;
    line-height: 56px;
    color: var(--ink);
    letter-spacing: 0.5px;
    white-space: nowrap;
  }
  .accent-band {
    position: absolute;
    left: 0; top: 232px;
    width: 100%;
    height: 16px;
    background: linear-gradient(90deg, var(--brand-blue-dark), var(--brand-blue-light) 45%, var(--brand-blue) 100%);
  }
  .contact-panel {
    position: absolute;
    left: 0; top: 248px;
    width: 100%;
    height: 256px;
    background: linear-gradient(180deg, var(--panel-charcoal), var(--panel-black) 70%);
  }
  .person-name {
    position: absolute;
    left: 56px;
    top: 26px;
    margin: 0;
    font-family: "Open Sans", sans-serif;
    font-weight: 600;
    font-size: 28px;
    line-height: 38px;
    color: var(--name-blue);
  }
  .contact-list {
    position: absolute;
    left: 56px;
    top: 96px;
    margin: 0;
    padding: 0;
    list-style: none;
    font-family: "Open Sans", sans-serif;
    font-size: 22px;
    line-height: 30px;
    color: var(--contact-white);
  }
  .contact-list li {
    display: flex;
    align-items: center;
    gap: 10px;
  }
  .contact-icon {
    width: 20px;
    height: 20px;
    flex: none;
    fill: var(--name-blue);
  }
</style>
</head>
<body>
  <div class="business-card">
    <header class="brand-area">
      <div class="brand-square"></div>
      <h1 class="brand-name">Halvorsen Associates,LLC</h1>
    </header>
    <div class="accent-band"></div>
    <section class="contact-panel">
      <h2 class="person-name">Marcus D. Halvorsen</h2>
      <ul class="contact-list">
        <li>
          <svg class="contact-icon" viewBox="0 0 20 20" aria-hidden="true"><rect x="5" y="1" width="10" height="18" rx="2"/><rect x="7" y="3" width="6" height="6" fill="#0f1114"/></svg>
          256-555-0187
        </li>
        <li>
          <svg class="contact-icon" viewBox="0 0 20 20" aria-hidden="true"><rect x="5" y="2" width="10" height="5"/><rect x="1" y="7" width="18" height="8" rx="2"/><rect x="5" y="12" width="10" height="6" fill="#f2f2f2"/></svg>
          256-555-0142
        </li>
        <li>
          <svg class="contact-icon" viewBox="0 0 20 20" aria-hidden="true"><rect x="1" y="4" width="18" height="13" rx="1"/><path d="M1 5 L10 12 L19 5" stroke="#0f1114" stroke-width="1.5" fill="none"/></svg>
          marcushalvorsen@mailbrook.test
        </li>
        <li>
          <svg class="contact-icon" viewBox="0 0 20 20" aria-hidden="true"><path d="M10 2 L19 10 L16 10 L16 18 L12 18 L12 13 L8 13 L8 18 L4 18 L4 10 L1 10 Z"/></svg>
          348 Birch Meadow Drive Hartwell AL 35612
        </li>
      </ul>
    </section>
  </div>
</body>
</html>
```